UK Vitamin Company Needs First Newspaper Advert

We are a small family run vitamin business called Brisk Nutrients, with a loyal customer base of women over 50 years old. As the winter approaches we want to run our first magazine advert to highlight our winter sale on our full vitamin range. This will ultimately be a 100mm x 77mm advert.

It need to be clean, simple, with a bit of energy - like our brand.

It needs to mention that we are offering up to 50% off our normal prices

It needs to call out the website: brisknutrients.example

It needs to feature the product and the brand logo

The attached files include the logo, and an example of our packaging.

Target Market(s)

Female over 50 (but often also men, so not overtly feminine)

Industry/Entity Type

Health And Wellness

Requirements
Must have
• Needs to really stand out in a cluttered space!
• 1.The brand logo prominently displayed (logo attached)
• 2.Some of the product/packs featured (selection attached)
• 3. Include the headline: Your family needs vitamins, Our family has them
• 4. Include the subheadline: The Brisk Nutrient Winter Sale is Now On
• 5. Include the offer: Get £5 off your first order and free shipping! Use code BRISKFROST

```html
<!DOCTYPE html>
<html lang="en">
<head>
<meta charset="utf-8">
<title>Brisk Nutrients – Winter Sale Advert</title>
<link href="https://fonts.googleapis.com/css2?family=Oswald:wght@400;600;700&family=Lato:wght@300;400&family=Montserrat:wght@500&display=swap" rel="stylesheet">
<style>
  :root {
    --brand-orange: #f07421;
    --brand-green: #1fa34a;
    --ink-grey: #555a5c;
    --pill-black: #2b2b2b;
    --paper: #ffffff;
    --mint-light: #eef8ea;
    --badge-ink: #17331f;
  }
  html, body {
    margin: 0;
    padding: 0;
    width: 1200px;
    height: 1029px;
    overflow: hidden;
    background: var(--paper);
  }
  .advert {
    position: absolute;
    left: 0;
    top: 53px;
    width: 1200px;
    height: 923px;
    overflow: hidden;
    background:
      radial-gradient(ellipse 520px 420px at 960px 120px, rgba(143, 211, 106, 0.85), rgba(143, 211, 106, 0) 75%),
      radial-gradient(ellipse 400px 300px at 1150px 300px, rgba(110, 195, 80, 0.7), rgba(110, 195, 80, 0) 80%),
      linear-gradient(120deg, #f9fcf7 0%, var(--mint-light) 45%, #c9ebb5 100%);
    font-family: "Lato", sans-serif;
  }
  .leaf-decoration {
    position: absolute;
    left: 760px;
    top: 0;
    width: 440px;
    height: 420px;
    background: radial-gradient(circle at 60% 40%, rgba(120, 200, 90, 0.35), rgba(120, 200, 90, 0) 70%);
  }
  .wave {
    position: absolute;
    left: 0;
    top: 0;
    width: 1200px;
    height: 923px;
  }
  .brand-name {
    position: absolute;
    left: 0;
    width: 754px;
    top: 92px;
    text-align: center;
    font-family: "Oswald", sans-serif;
    font-weight: 600;
    font-size: 68px;
    line-height: 1;
    color: var(--brand-orange);
    white-space: nowrap;
  }
  .brand-name .brand-dot {
    display: inline-block;
    width: 24px;
    height: 24px;
    border-radius: 50%;
    background: var(--brand-green);
    margin-right: 14px;
    vertical-align: middle;
  }
  .headline {
    position: absolute;
    left: 59px;
    top: 196px;
    margin: 0;
    font-family: "Oswald", sans-serif;
    font-weight: 600;
    font-size: 53px;
    line-height: 1.1;
    color: var(--brand-green);
    white-space: nowrap;
  }
  .headline-answer {
    position: absolute;
    left: 57px;
    top: 248px;
    margin: 0;
    font-family: "Lato", sans-serif;
    font-weight: 400;
    font-size: 72px;
    line-height: 1;
    color: var(--ink-grey);
    white-space: nowrap;
  }
  .sale-pill {
    position: absolute;
    left: 62px;
    top: 343px;
    width: 634px;
    height: 53px;
    border-radius: 27px;
    background: var(--pill-black);
    color: #f2f2f2;
    font-family: "Lato", sans-serif;
    font-weight: 300;
    font-size: 27px;
    line-height: 53px;
    text-align: center;
    white-space: nowrap;
    z-index: 2;
  }
  .offer-get {
    position: absolute;
    left: 89px;
    top: 472px;
    font-family: "Oswald", sans-serif;
    font-weight: 700;
    font-size: 84px;
    line-height: 1;
    color: var(--brand-orange);
  }
  .offer-amount {
    position: absolute;
    left: 240px;
    top: 392px;
    font-family: "Oswald", sans-serif;
    font-weight: 700;
    font-size: 182px;
    line-height: 1;
    color: var(--brand-orange);
    letter-spacing: 0;
  }
  .offer-off {
    position: absolute;
    left: 410px;
    top: 458px;
    width: 144px;
    height: 62px;
    transform: rotate(-90deg);
    font-family: "Lato", sans-serif;
    font-weight: 300;
    font-size: 70px;
    line-height: 62px;
    color: var(--brand-green);
    text-align: center;
  }
  .offer-terms {
    position: absolute;
    left: 54px;
    top: 576px;
    font-family: "Montserrat", sans-serif;
    font-weight: 500;
    font-size: 26px;
    color: var(--ink-grey);
    white-space: nowrap;
  }
  .code-badge {
    position: absolute;
    left: 180px;
    top: 610px;
    width: 220px;
    height: 220px;
    border-radius: 50%;
    background: var(--brand-green);
    border: 8px solid var(--paper);
    display: flex;
    flex-direction: column;
    align-items: center;
    justify-content: center;
    font-family: "Oswald", sans-serif;
    font-weight: 600;
    font-size: 33px;
    line-height: 1.2;
    z-index: 2;
  }
  .code-badge .code-label { color: var(--badge-ink); }
  .code-badge .code-value { color: var(--paper); font-size: 31px; }
  .website {
    position: absolute;
    left: 133px;
    top: 856px;
    font-family: "Lato", sans-serif;
    font-weight: 400;
    font-size: 30px;
    color: var(--paper);
    white-space: nowrap;
  }
  .product-pack {
    position: absolute;
    border-radius: 24px;
    background: linear-gradient(160deg, #ffffff 0%, #eef0f0 55%, #d6d9d9 100%);
    box-shadow: 0 6px 14px rgba(0, 0, 0, 0.18);
  }
  .pack-back-right { left: 958px; top: 461px; width: 195px; height: 421px; z-index: 1; }
  .pack-back-centre { left: 717px; top: 380px; width: 253px; height: 492px; z-index: 2; }
  .pack-front-left { left: 544px; top: 481px; width: 274px; height: 416px; z-index: 3; }
</style>
</head>
<body>
  <main class="advert">
    <div class="leaf-decoration" role="img" aria-label="Soft green leaf pattern background"></div>

    <svg class="wave" viewBox="0 0 1200 923" aria-hidden="true">
      <path d="M0,718 C200,770 380,700 560,605 C760,500 960,395 1200,388 L1200,923 L0,923 Z" fill="var(--brand-green)"/>
      <path d="M0,758 C200,805 390,728 570,630 C770,525 960,415 1200,408 L1200,923 L0,923 Z" fill="var(--paper)"/>
      <path d="M0,771 C200,818 395,740 575,643 C775,537 965,427 1200,420 L1200,923 L0,923 Z" fill="var(--brand-orange)"/>
    </svg>

    <div class="brand-name"><span class="brand-dot"></span>Brisk Nutrients</div>

    <h1 class="headline">YOUR FAMILY NEEDS VITAMINS</h1>
    <h2 class="headline-answer">Our family has them</h2>

    <div class="sale-pill">The Brisk Nutrient Winter Sale is Now On</div>

    <div class="offer-get">GET</div>
    <div class="offer-amount">£5</div>
    <div class="offer-off">OFF</div>
    <div class="offer-terms">your first order and free shipping!</div>

    <div class="code-badge">
      <span class="code-label">Use code</span>
      <span class="code-value">BRISKFROST</span>
    </div>

    <div class="website">www.brisknutrients.example</div>

    <div class="product-pack pack-back-right" role="img" aria-label="White supplement pack with blue antioxidant label"></div>
    <div class="product-pack pack-back-centre" role="img" aria-label="White supplement pack with orange probiotic label"></div>
    <div class="product-pack pack-front-left" role="img" aria-label="White supplement pack with teal joint care label"></div>
  </main>
</body>
</html>
```